Flyer für Computer Service
Zielgruppe
Privathaushalte und kleinere Firmen.
Wir möchten damit neue Kunden für unsere Dienstleistungen gewinnen.
Aufgabenstellung
Wir möchten mit diesem Flyer speziell unsere Computer Service Dienstleistungen bewerben.
Im wesentlichen werden folgende 3 Kategorieren von Dienstleistungen angeboten:
- Fernwartung
- Reparaturen
- Neuinstallationen, Backups und Virenentfernung
Fernwartung und Reparaturen bieten wir zu "ab EUR xx.-" Preisen an und Neuinstallationen, Backups und Virenentfernung zu Pauschalen.

```html
<!DOCTYPE html>
<html lang="de">
<head>
<meta charset="utf-8">
<title>Relvano – PC Service Flyer</title>
<link rel="stylesheet" href="https://fonts.googleapis.com/css2?family=Titan+One&family=Ubuntu:wght@500;700&family=Arimo:wght@700&display=swap">
<style>
  :root {
    --orange: #f47b10;
    --orange-light: #ffa23a;
    --blue: #2f80d2;
    --blue-dark: #1a56a6;
    --blue-deep: #0f3f86;
    --grey: #c8c9cb;
    --white: #ffffff;
    --ink: #1d3f7a;
  }
  * { box-sizing: border-box; margin: 0; padding: 0; }
  html, body { width: 849px; height: 1200px; overflow: hidden; background: var(--white); }
  .flyer {
    position: relative; width: 849px; height: 1200px; overflow: hidden;
    font-family: "Arimo", Arial, sans-serif;
  }
  .backdrop { position: absolute; inset: 0; }

  .portrait {
    position: absolute; left: 34px; top: 0; width: 230px; height: 272px;
    background: linear-gradient(160deg, #d9dde2 0%, #8c939c 55%, #3d434b 100%);
    border: 4px solid var(--white); border-top: 0;
    transform: skewX(-4deg);
  }
  .headline {
    position: absolute; left: 320px; top: 55px; width: 500px; text-align: center;
    font-family: "Titan One", sans-serif; font-size: 44px; letter-spacing: 1px;
    color: var(--blue); -webkit-text-stroke: 2px var(--white);
    text-shadow: 3px 4px 0 rgba(0,0,0,.35);
    transform: rotate(-2deg);
  }
  .tagline {
    position: absolute; right: 52px; top: 138px; text-align: right;
    font-family: "Ubuntu", sans-serif; font-weight: 700; font-size: 25px; line-height: 31px;
    color: var(--white); text-shadow: 2px 2px 2px rgba(0,0,0,.4);
  }
  .hardware {
    position: absolute; left: 455px; top: 232px; width: 340px; height: 285px;
    border-radius: 8px;
    background: linear-gradient(135deg, #7a7d83 0%, #44474c 45%, #24262a 100%);
  }

  .service {
    position: absolute; border: 4px solid var(--white);
    box-shadow: 0 0 0 1px rgba(0,0,0,.12);
    color: var(--white);
  }
  .service--blue { background: linear-gradient(180deg, #57a0e6 0%, var(--blue) 45%, var(--blue-dark) 100%); }
  .service--orange { background: linear-gradient(180deg, var(--orange-light) 0%, var(--orange) 50%, #e06400 100%); }
  .service__title {
    height: 46px; padding: 14px 14px 0;
    font-family: "Ubuntu", sans-serif; font-weight: 700; font-size: 19px; letter-spacing: .5px;
    background: rgba(255,255,255,.12);
  }
  .service--blue .service__title { color: var(--orange); text-shadow: 1px 1px 0 var(--white); }
  .service--orange .service__title { color: var(--ink); text-shadow: 1px 1px 0 rgba(255,255,255,.6); }
  .service__text { padding: 12px 14px 0; font-size: 12.5px; line-height: 16px; }
  .service--narrow .service__text { padding-right: 30px; }
  .service__price {
    position: absolute; left: 0; right: 0; bottom: 0; height: 58px;
    padding: 8px 12px 0; background: rgba(255,255,255,.14);
    font-family: "Ubuntu", sans-serif; font-weight: 700; white-space: nowrap;
  }
  .price__from { font-size: 26px; text-shadow: -1px -1px 0 var(--white), 1px 1px 0 var(--white), 1px -1px 0 var(--white), -1px 1px 0 var(--white); }
  .price__amount { font-size: 40px; margin-left: 6px; text-shadow: -2px -2px 0 var(--white), 2px 2px 0 var(--white), 2px -2px 0 var(--white), -2px 2px 0 var(--white); }
  .service--blue .price__from { color: var(--blue-deep); }
  .service--blue .price__amount { color: var(--orange); }
  .service--orange .price__from,
  .service--orange .price__amount { color: var(--blue-dark); }

  .benefits {
    position: absolute; left: 535px; top: 550px; list-style: none;
    font-family: "Ubuntu", sans-serif; font-weight: 700; font-size: 21px; line-height: 26px;
    color: var(--white); text-shadow: 1px 1px 2px rgba(0,0,0,.45);
  }
  .benefits li { position: relative; padding-left: 32px; }
  .benefits li::before {
    content: ""; position: absolute; left: 0; top: 7px; width: 12px; height: 12px;
    background: var(--orange-light); border: 2px solid var(--white);
  }

  .brand {
    position: absolute; left: 52px; top: 1000px;
    font-family: "Ubuntu", sans-serif; font-weight: 700; font-size: 96px; line-height: 1;
    color: var(--blue-deep);
  }
  .brand__web {
    position: absolute; left: 240px; top: 1106px;
    font-family: "Ubuntu", sans-serif; font-weight: 700; font-size: 20px; color: var(--white);
  }
  .brand__address {
    position: absolute; left: 56px; top: 1153px;
    font-family: "Ubuntu", sans-serif; font-weight: 700; font-size: 16px; color: var(--white);
  }
  .contact {
    position: absolute; left: 548px; top: 1048px; width: 300px;
    font-family: "Ubuntu", sans-serif; font-weight: 700; color: var(--white);
    transform: rotate(-13deg); transform-origin: left top;
    text-shadow: 1px 1px 2px rgba(0,0,0,.3);
  }
  .contact__label { font-size: 26px; }
  .contact__phone { font-size: 34px; line-height: 38px; }
  .contact__mail { font-size: 16px; }
</style>
</head>
<body>
<main class="flyer">
  <svg class="backdrop" width="849" height="1200" viewBox="0 0 849 1200" aria-hidden="true">
    <defs>
      <radialGradient id="sunburst" cx="0.72" cy="0.45" r="0.7">
        <stop offset="0" stop-color="#ffa540"/>
        <stop offset="1" stop-color="#f06f05"/>
      </radialGradient>
      <linearGradient id="skyBlue" x1="0" y1="0" x2="0" y2="1">
        <stop offset="0" stop-color="#2f80d2"/>
        <stop offset="1" stop-color="#1a56a6"/>
      </linearGradient>
    </defs>
    <rect width="849" height="390" fill="url(#sunburst)"/>
    <polygon points="0,0 849,0 849,22 330,22 285,390 0,390" fill="url(#skyBlue)"/>
    <polygon points="330,22 338,22 293,390 285,390" fill="#ffffff"/>
    <rect y="384" width="849" height="8" fill="#ffffff"/>
    <rect y="392" width="849" height="590" fill="#ffffff"/>
    <polygon points="510,392 849,392 849,675 510,675" fill="#c8c9cb"/>
    <path d="M510,560 Q680,470 849,520 L849,675 L510,675 Z" fill="#b4b6b9"/>
    <rect y="982" width="849" height="218" fill="url(#skyBlue)"/>
    <polygon points="0,990 420,990 390,1130 0,1130" fill="#f47b10"/>
    <polygon points="849,1020 849,1200 520,1200" fill="#f47b10"/>
    <rect y="976" width="849" height="8" fill="#ffffff"/>
  </svg>

  <div class="portrait" role="img" aria-label="Foto eines Servicetechnikers im Anzug mit Laptop"></div>

  <h1 class="headline">PC PROBLEME ???</h1>
  <p class="tagline">..kein Problem, wir helfen Ihnen Sofort<br>Professinal, Schnell und Günstig</p>

  <div class="hardware" role="img" aria-label="Produktfoto: Desktop-PC mit Tastatur, Maus und Laptop"></div>

  <section class="service service--blue service--narrow" style="left:8px;top:402px;width:250px;height:272px;">
    <h2 class="service__title">REPERATUREN</h2>
    <p class="service__text">Hier könnte ihr Feintext stehen der Ihre Leistung genau erklährt. Hier könnte ihr Feintext stehen der Ihre Leistung genau erklährt. Hier könnte ihr Feintext stehen der Ihre Leistung genau erklährt.der Ihre Leistung genau erklährt. Hier könnte ihr Feintext stehen der Ihre Leistung genau</p>
    <div class="service__price"><span class="price__from">schon ab</span><span class="price__amount">59 €</span></div>
  </section>

  <section class="service service--orange service--narrow" style="left:267px;top:402px;width:245px;height:272px;">
    <h2 class="service__title">FERNWARTUNG</h2>
    <p class="service__text">Hier könnte ihr Feintext stehen der Ihre Leistung genau erklährt. Hier könnte ihr Feintext stehen der Ihre Leistung genau erklährt. Hier könnte ihr Feintext stehen der Ihre Leistung genau erklährt.der Ihre Leistung genau erklährt. Hier könnte ihr Feintext stehen der Ihre Leistung genau</p>
    <div class="service__price"><span class="price__from">schon ab</span><span class="price__amount">59 €</span></div>
  </section>

  <ul class="benefits">
    <li>Schneller Service</li>
    <li>Fixe Tiefpreise</li>
    <li>Kompetente Beratung</li>
    <li>Professioneller Support</li>
  </ul>

  <section class="service service--orange" style="left:8px;top:697px;width:272px;height:265px;">
    <h2 class="service__title">NEUINSTALLATIONEN</h2>
    <p class="service__text">Hier könnte ihr Feintext stehen der Ihre Leistung genau erklährt. Hier könnte ihr Feintext stehen der Ihre Leistung genau erklährt. Hier könnte ihr Feintext stehen der Ihre Leistung genau erklährt. Hier könnte ihr Feintext der Ihre Leistung genau erklährt. Hier könnte ihr Feintext stehen der Ihre Leistung genau</p>
    <div class="service__price"><span class="price__from">schon ab</span><span class="price__amount">59 €</span></div>
  </section>

  <section class="service service--blue" style="left:293px;top:697px;width:270px;height:265px;">
    <h2 class="service__title">BACKUPS</h2>
    <p class="service__text">Hier könnte ihr Feintext stehen der Ihre Leistung genau erklährt. Hier könnte ihr Feintext stehen der Ihre Leistung genau erklährt. Hier könnte ihr Feintext stehen der Ihre Leistung genau erklährt. Hier könnte ihr Feintext der Ihre Leistung genau erklährt. Hier könnte ihr Feintext stehen der Ihre Leistung genau</p>
    <div class="service__price"><span class="price__from">schon ab</span><span class="price__amount">59 €</span></div>
  </section>

  <section class="service service--orange" style="left:578px;top:697px;width:263px;height:265px;">
    <h2 class="service__title">Virenentfernung</h2>
    <p class="service__text">Hier könnte ihr Feintext stehen der Ihre Leistung genau erklährt. Hier könnte ihr Feintext stehen der Ihre Leistung genau erklährt. Hier könnte ihr Feintext stehen der Ihre Leistung genau erklährt. Hier könnte ihr Feintext der Ihre Leistung genau erklährt. Hier könnte ihr Feintext stehen der Ihre Leistung genau</p>
    <div class="service__price"><span class="price__from">schon ab</span><span class="price__amount">59 €</span></div>
  </section>

  <div class="brand">relvano</div>
  <div class="brand__web">www.relvano.ch</div>
  <p class="brand__address">Relvano GmbH - Musterstr.12 - Musterhausen 33667</p>

  <div class="contact">
    <div class="contact__label">INFOS UNTER :</div>
    <div class="contact__phone">0800 / 4455667</div>
    <div class="contact__mail">Email : info@relvano.ch</div>
  </div>
</main>
</body>
</html>
```